Animated GIF banner for mobile app

We need a GIF Banner designed that alternates between two different ads.

Details are;
Pixel Size (W X H) 300 X 250
Minimum DPI 72dpi
File Size 40kb
File Size (Rich Media) 150kb

Ad 1 Text:
Lost super? More than one super fund? Contact us

Ad 2 Text:
Time to review your home loan? Contact us

Target Market(s)

30-55 year olds

Industry/Entity Type

Financial Service

Font styles to use
Sans Serif

Colors
0555a3
3176b5
85abd2

```html
<!DOCTYPE html>
<html lang="en">
<head>
<meta charset="utf-8">
<title>Harlow Banks – Banner Set</title>
<link rel="stylesheet" href="https://fonts.googleapis.com/css2?family=Bebas+Neue&family=PT+Sans:wght@400;700&family=PT+Sans+Narrow:wght@700&family=Roboto:wght@700&display=swap">
<style>
:root{
  --brand-blue:#0555a3;
  --mid-blue:#3176b5;
  --soft-blue:#85abd2;
  --pale-blue:#c6daef;
  --deep-blue:#0a4686;
  --cta-yellow:#f8b810;
  --ink:#1a1a1a;
  --white:#ffffff;
  --page:#e9eaec;
}
*{box-sizing:border-box;margin:0;padding:0}
html,body{width:1200px;height:1200px;overflow:hidden;background:var(--page)}
.stage{position:absolute;left:0;top:0;width:1000px;height:1000px;transform:scale(1.2);transform-origin:0 0}
.set-label{position:absolute;font:400 28px/1 "PT Sans",sans-serif;color:var(--ink)}
.banner{position:absolute;width:297px;height:248px;overflow:hidden;background:var(--brand-blue);box-shadow:0 14px 16px -10px rgba(0,0,0,.45)}
.banner svg.bg{position:absolute;left:0;top:0}
.header{position:absolute;left:0;top:0;width:297px;height:46px;background:var(--white)}
.brand{position:absolute;left:8px;top:9px;display:flex;align-items:center;gap:6px;color:var(--brand-blue);font-family:"PT Sans",sans-serif;font-weight:400}
.brand-dot{width:24px;height:24px;border-radius:50%;background:var(--brand-blue)}
.brand-name{font-size:14px;line-height:14px}
.brand-name small{display:block;font-size:9px;line-height:11px}
.headline-classic{position:absolute;font:700 40px/52px "PT Sans Narrow",sans-serif;color:var(--white);letter-spacing:-.5px}
.sub-classic{position:absolute;font:400 17px/18px "PT Sans",sans-serif;color:var(--white);text-align:right}
.cta-classic{position:absolute;left:177px;top:202px;width:93px;height:25px;background:var(--deep-blue);color:var(--white);font:700 13px/25px "PT Sans Narrow",sans-serif;text-align:center;box-shadow:2px 3px 4px rgba(0,0,0,.45)}
.title-box{position:absolute;background:var(--pale-blue);border-radius:3px;text-align:center;font-family:"Bebas Neue",sans-serif;color:var(--brand-blue)}
.title-box .big{display:block}
.title-box .small{display:block;letter-spacing:4px}
.sub-bold{position:absolute;font:400 21px/24px "Bebas Neue",sans-serif;color:var(--white);text-align:center;letter-spacing:.3px}
.cta-pill{position:absolute;height:26px;border-radius:13px;background:var(--cta-yellow);color:var(--ink);font:700 13px/26px "Roboto",sans-serif;text-align:center;letter-spacing:.2px}
.cta-pill::after{content:" »";font-size:16px}
.photo{position:absolute}
.photo-desk{left:0;top:46px;width:152px;height:202px;background:linear-gradient(160deg,#ffffff 0%,#d9c98f 35%,#8a8e96 70%,#ffffff 100%)}
.photo-keys{left:0;top:40px;width:150px;height:208px;background:linear-gradient(170deg,#3f86d6 0%,#9dc3ea 35%,#c8b27a 65%,#6d5a3e 100%)}
.white-side{position:absolute;left:0;top:0;width:152px;height:248px;background:var(--white)}
.right-panel{position:absolute;left:152px;top:0;width:145px;height:248px;background:var(--brand-blue)}
</style>
</head>
<body>
<main class="stage">

  <span class="set-label" style="left:36px;top:14px">1</span>
  <span class="set-label" style="left:363px;top:14px">2</span>
  <span class="set-label" style="left:36px;top:322px">1</span>
  <span class="set-label" style="left:363px;top:322px">2</span>
  <span class="set-label" style="left:36px;top:638px">1</span>
  <span class="set-label" style="left:363px;top:638px">2</span>
  <span class="set-label" style="left:676px;top:216px">1</span>
  <span class="set-label" style="left:676px;top:532px">2</span>

  <!-- Classic curve: ad 1 -->
  <section class="banner" style="left:36px;top:46px">
    <svg class="bg" width="297" height="248" viewBox="0 0 297 248">
      <rect y="46" width="297" height="202" fill="var(--brand-blue)"/>
      <path d="M232 46 C205 150 130 210 60 248 L297 248 L297 46 Z" fill="var(--mid-blue)"/>
      <path d="M232 46 C205 150 130 210 60 248" fill="none" stroke="rgba(0,0,0,.18)" stroke-width="4"/>
    </svg>
    <div class="header"><div class="brand"><span class="brand-dot"></span><span class="brand-name">Harlow Banks<small>Financial Solutions</small></span></div></div>
    <h2 class="headline-classic" style="left:34px;top:56px">LOST</h2>
    <h2 class="headline-classic" style="left:14px;top:110px">SUPER?</h2>
    <p class="sub-classic" style="left:150px;top:157px;width:138px">More than one super fund?</p>
    <div class="cta-classic">CONTACT US</div>
  </section>

  <!-- Classic curve: ad 2 -->
  <section class="banner" style="left:352px;top:46px">
    <svg class="bg" width="297" height="248" viewBox="0 0 297 248">
      <rect y="46" width="297" height="202" fill="var(--brand-blue)"/>
      <path d="M232 46 C205 150 130 210 60 248 L297 248 L297 46 Z" fill="var(--mid-blue)"/>
      <path d="M232 46 C205 150 130 210 60 248" fill="none" stroke="rgba(0,0,0,.18)" stroke-width="4"/>
    </svg>
    <div class="header"><div class="brand"><span class="brand-dot"></span><span class="brand-name">Harlow Banks<small>Financial Solutions</small></span></div></div>
    <h2 class="headline-classic" style="left:8px;top:56px">TIME TO</h2>
    <h2 class="headline-classic" style="left:10px;top:110px">REVIEW</h2>
    <p class="sub-classic" style="left:150px;top:157px;width:124px">your<br>home loan?</p>
    <div class="cta-classic">CONTACT US</div>
  </section>

  <!-- Bold box: ad 1 -->
  <section class="banner" style="left:36px;top:354px">
    <div class="header"><div class="brand"><span class="brand-dot"></span><span class="brand-name">Harlow Banks<small>Financial Solutions</small></span></div></div>
    <div class="title-box" style="left:22px;top:79px;width:130px;height:103px">
      <span class="big" style="font-size:72px;line-height:70px">LOST</span>
      <span class="small" style="font-size:30px;line-height:28px">SUPER?</span>
    </div>
    <p class="sub-bold" style="left:166px;top:88px;width:120px">MORE<br>THAN ONE<br>SUPER FUND?</p>
    <div class="cta-pill" style="left:157px;top:202px;width:131px">CONTACT US</div>
  </section>

  <!-- Bold box: ad 2 -->
  <section class="banner" style="left:352px;top:354px">
    <div class="header"><div class="brand"><span class="brand-dot"></span><span class="brand-name">Harlow Banks<small>Financial Solutions</small></span></div></div>
    <div class="title-box" style="left:22px;top:79px;width:130px;height:103px">
      <span class="big" style="font-size:72px;line-height:70px">TIME</span>
      <span class="small" style="font-size:30px;line-height:28px;letter-spacing:0">TO REVIEW</span>
    </div>
    <p class="sub-bold" style="left:166px;top:100px;width:120px">YOUR<br>HOME LOAN?</p>
    <div class="cta-pill" style="left:157px;top:202px;width:131px">CONTACT US</div>
  </section>

  <!-- Split photo: ad 1 -->
  <section class="banner" style="left:36px;top:670px">
    <div class="white-side"></div>
    <div class="photo photo-desk" role="img" aria-label="Model house and calculator in a hand"></div>
    <div class="brand"><span class="brand-dot"></span><span class="brand-name">Harlow Banks<small>Financial Solutions</small></span></div>
    <div class="right-panel"></div>
    <div class="title-box" style="left:165px;top:12px;width:122px;height:106px">
      <span class="big" style="font-size:70px;line-height:70px">LOST</span>
      <span class="small" style="font-size:31px;line-height:30px">SUPER?</span>
    </div>
    <p class="sub-bold" style="left:160px;top:126px;width:132px">MORE<br>THAN ONE<br>SUPER FUND?</p>
    <div class="cta-pill" style="left:160px;top:211px;width:131px">CONTACT US</div>
  </section>

  <!-- Split photo: ad 2 -->
  <section class="banner" style="left:352px;top:670px">
    <div class="white-side"></div>
    <div class="photo photo-desk" role="img" aria-label="Model house and calculator in a hand"></div>
    <div class="brand"><span class="brand-dot"></span><span class="brand-name">Harlow Banks<small>Financial Solutions</small></span></div>
    <div class="right-panel"></div>
    <div class="title-box" style="left:165px;top:12px;width:122px;height:106px">
      <span class="big" style="font-size:70px;line-height:70px">TIME</span>
      <span class="small" style="font-size:31px;line-height:30px;letter-spacing:0">TO REVIEW</span>
    </div>
    <p class="sub-bold" style="left:160px;top:138px;width:132px">YOUR<br>HOME LOAN?</p>
    <div class="cta-pill" style="left:160px;top:211px;width:131px">CONTACT US</div>
  </section>

  <!-- Keys photo: ad 1 -->
  <section class="banner" style="left:672px;top:247px;background:var(--white)">
    <div class="photo photo-keys" role="img" aria-label="Hand holding house keys in front of a home"></div>
    <svg class="bg" width="297" height="248" viewBox="0 0 297 248">
      <path d="M143 0 C126 80 128 170 160 248 L297 248 L297 0 Z" fill="var(--mid-blue)"/>
      <path d="M152 0 C136 80 138 170 170 248 L297 248 L297 0 Z" fill="var(--brand-blue)"/>
    </svg>
    <div class="brand"><span class="brand-dot"></span><span class="brand-name">Harlow Banks<small>Financial Solutions</small></span></div>
    <div class="title-box" style="left:178px;top:22px;width:102px;height:78px;color:var(--mid-blue)">
      <span class="big" style="font-size:30px;line-height:36px;margin-top:4px">LOST</span>
      <span class="big" style="font-size:30px;line-height:36px">SUPER?</span>
    </div>
    <p class="sub-bold" style="left:160px;top:128px;width:140px;font-size:24px;line-height:30px">MORE THAN ONE<br>SUPER FUND?</p>
    <div class="cta-pill" style="left:160px;top:208px;width:131px">CONTACT US</div>
  </section>

  <!-- Keys photo: ad 2 -->
  <section class="banner" style="left:672px;top:562px;background:var(--white)">
    <div class="photo photo-keys" role="img" aria-label="Hand holding house keys in front of a home"></div>
    <svg class="bg" width="297" height="248" viewBox="0 0 297 248">
      <path d="M143 0 C126 80 128 170 160 248 L297 248 L297 0 Z" fill="var(--mid-blue)"/>
      <path d="M152 0 C136 80 138 170 170 248 L297 248 L297 0 Z" fill="var(--brand-blue)"/>
    </svg>
    <div class="brand"><span class="brand-dot"></span><span class="brand-name">Harlow Banks<small>Financial Solutions</small></span></div>
    <div class="title-box" style="left:178px;top:22px;width:102px;height:78px;color:var(--mid-blue)">
      <span class="big" style="font-size:30px;line-height:36px;margin-top:4px">TIME TO</span>
      <span class="big" style="font-size:30px;line-height:36px">REVIEW</span>
    </div>
    <p class="sub-bold" style="left:160px;top:128px;width:140px;font-size:24px;line-height:30px">YOUR<br>HOME LOAN?</p>
    <div class="cta-pill" style="left:160px;top:208px;width:131px">CONTACT US</div>
  </section>

</main>
</body>
</html>
```